Simple Country Singer Website - TinBellRaven.com

We need a simple Wordpress site designed for our client Tin Bell Raven. Tin Bell Raven is a country and country rap artist who's elevating the genre to the next level with AI video and sound elements. We are looking for a Wordpress site to post new videos and tracks, to take donations, and to eventually link to our merch store.

The design we're looking for is simple, clean, mobile first, and designed to appeal to our audience.

Full project description: https://files.plovermesh.net/doc/7k-rtw-QPld4MxZa2Vn8HoJe5CtY-Wq3/view?tab=t.0

Target Market(s)

Our audience is mainly people 40+ in the United States who are country and country rap fans, and who have conservative values.

Industry/Entity Type

Music

Coding

Coded - Design and coding required

Number of Pages Required

1 page

Font styles to use
Sans Serif

Requirements
Must have
• Must be designed for Wordpress and be mobile first. Must incorporate existing Tin Bell Raven logo (see attached screenshot.) We will provide high quality .psd files soon
Nice to have
• Use existing Tin Bell Raven logo we will provide. Use hamburger menu on mobile.
Should not have
• Slow loading elements, dark background, elements that do not work on mobile

```html
<!DOCTYPE html>
<html lang="en">
<head>
<meta charset="utf-8">
<title>Tin Bell Raven — Home</title>
<link rel="stylesheet" href="https://fonts.googleapis.com/css2?family=Poppins:wght@400;500;600;700&display=swap">
<style>
:root{
  --ink:#1b1b1b;
  --dark:#1c1c1c;
  --paper:#ffffff;
  --mist:#f4f4f4;
  --line:#e4e4e4;
  --muted:#777;
  --accent:#7b2015;
  --ad-yellow:#f3d21a;
  --ad-blue:#14457c;
}
*{box-sizing:border-box;margin:0;padding:0}
html,body{width:1200px;height:4494px;overflow:hidden;background:var(--paper);font-family:"Poppins",sans-serif;color:var(--ink)}
.canvas{position:relative;width:1200px;height:4494px}
.board{position:absolute;top:48px;background:var(--paper);overflow:hidden}
.desktop{left:46px;width:854px;height:2877px}
.mobile{left:958px;width:184px;height:4444px}
.abs{position:absolute}
.dark{background:var(--dark);color:#fff}

/* photo placeholders */
.ph{border-radius:4px}
.ph-warm{background:radial-gradient(circle at 45% 35%,#f08a3a 0,#a8321a 35%,#2a0d08 80%)}
.ph-studio{background:linear-gradient(135deg,#6b5a4a,#2b2520 55%,#8a6a4a)}
.ph-blue{background:radial-gradient(circle at 50% 60%,#2d8fb4 0,#12384d 45%,#0b1419 90%)}
.ph-purple{background:radial-gradient(circle at 60% 30%,#c2318f 0,#4a1a4f 45%,#131018 90%)}
.ph-grey{background:linear-gradient(135deg,#d9dcdf,#7d8388 60%,#3b3f44)}
.ph-stage{background:linear-gradient(160deg,#1d1a3a,#ad3a2a 60%,#f0a040)}
.ph-hero{background:linear-gradient(120deg,#0d1230 0,#1d2a5c 40%,#8b2a40 70%,#d04a30 100%)}

/* header */
.d-header{left:0;top:0;width:854px;height:62px;border-bottom:1px solid var(--line);display:flex;align-items:center}
.brand{font-weight:700;color:var(--accent);letter-spacing:.02em;line-height:1;display:flex;align-items:center;gap:4px}
.d-nav{position:absolute;top:24px;display:flex;font-size:10px;font-weight:500;letter-spacing:.04em}
.d-nav a{position:absolute;white-space:nowrap;color:var(--ink);text-decoration:none}
.d-nav a.on{color:var(--accent);border-bottom:1px solid var(--accent)}
.btn-login{position:absolute;left:649px;top:9px;width:127px;height:37px;background:var(--accent);color:#fff;border-radius:6px;font-size:10px;font-weight:500;display:flex;align-items:center;justify-content:center;letter-spacing:.04em}

/* hero */
.d-hero{left:0;top:62px;width:854px;height:435px;background:var(--mist)}
.hero-card{left:81px;top:32px;width:431px;height:339px;border-radius:8px}
.badge-new{position:absolute;left:24px;top:18px;background:var(--accent);color:#fff;font-size:8px;padding:3px 8px;border-radius:2px}
.watch{position:absolute;left:168px;top:242px;width:96px;height:24px;border-radius:6px;background:#fff;font-size:8px;display:flex;align-items:center;justify-content:center;color:#333}
.dashes{position:absolute;left:38px;right:38px;top:308px;display:flex;gap:10px}
.dashes i{flex:1;height:2px;background:rgba(255,255,255,.35)}
.dashes i.on{background:#fff}
.hero-list{left:536px;top:32px;width:239px}
.hl-item{display:flex;gap:10px;height:73px;border-bottom:1px solid var(--line);padding-top:4px}
.hl-item .ph{width:42px;height:42px;flex:none;border-radius:3px}
.hl-item h4{font-size:8.5px;font-weight:500;line-height:1.6}
.hl-item p{font-size:7px;color:var(--muted);margin-top:6px}

/* episodes */
.sec-title{font-size:15px;font-weight:600;letter-spacing:.02em}
.d-episodes{left:0;top:497px;width:854px;height:399px}
.view-all{font-size:9px;letter-spacing:.04em;display:flex;align-items:center;gap:6px}
.ep-card{position:absolute;top:104px;width:205px}
.ep-card .ph{height:157px;border-radius:6px}
.ep-date{font-size:8px;margin-top:16px}
.ep-title{font-size:8.5px;font-weight:600;line-height:1.7;margin-top:8px}
.ep-desc{font-size:7.5px;color:#bbb;margin-top:8px}

/* ad */
.ad-label{left:0;width:854px;top:982px;text-align:center;font-size:9px;letter-spacing:.12em;color:#777}
.ad{left:106px;top:1015px;width:651px;height:81px;display:flex;overflow:hidden}
.ad-photo{width:190px;background:linear-gradient(90deg,#5a2a1a,#c89060 50%,#3a2a22)}
.ad-body{flex:1;background:var(--ad-blue);position:relative;color:var(--ad-yellow)}
.ad-q{position:absolute;left:8px;top:22px;background:var(--ad-yellow);color:var(--ad-blue);font-size:11px;font-weight:600;padding:3px 7px}
.ad-head{position:absolute;left:155px;top:6px;font-size:17px;font-weight:500;line-height:1.25}
.ad-sub{position:absolute;left:165px;top:58px;font-size:11px;color:#fff}
.ad-sub b{color:#fff;font-weight:700;letter-spacing:.08em}

/* news */
.news-head{left:0;top:1180px;width:854px;height:44px;border-bottom:1px solid var(--line);text-align:center;font-size:15px;font-weight:600}
.news-card{position:absolute;width:219px;background:#fff;border-radius:6px;box-shadow:0 2px 10px rgba(0,0,0,.12);padding:12px 14px}
.news-card .ph{height:146px;border-radius:3px}
.news-card h5{font-size:9px;font-weight:400;line-height:1.7;margin-top:14px;height:48px}
.news-card p{font-size:8.5px;color:#666;margin-top:12px;padding-left:2px}

/* shorts */
.d-shorts{left:0;top:1850px;width:854px;height:399px}
.short-txt{position:absolute;font-size:10px;line-height:1.75;color:#e8e8e8}
.short-img{position:absolute;border-radius:4px}
.short-over{position:absolute;left:14px;bottom:14px;right:10px;font-size:10px;line-height:1.6;color:#fff}

/* more */
.more{left:0;top:2605px;width:854px;text-align:center;font-size:9.5px;letter-spacing:.06em;font-weight:500}

/* footer */
.d-footer{left:0;top:2688px;width:854px;height:189px}
.f-nav{position:absolute;display:flex;gap:29px;font-size:9.5px;letter-spacing:.04em}
.socials{position:absolute;display:flex;gap:8px}
.socials i{width:22px;height:22px;border-radius:50%;background:#fff;display:block}
.f-rule{position:absolute;height:1px;background:#555}
.copy{position:absolute;font-size:10px;color:#ddd;text-align:center}

/* mobile */
.m-header{left:0;top:0;width:184px;height:32px;display:flex;align-items:center;justify-content:space-between;padding:0 10px}
.burger{width:12px;display:flex;flex-direction:column;gap:2px}
.burger i{height:1px;background:var(--ink);display:block}
.m-hero{left:11px;top:40px;width:162px;height:129px;border-radius:6px}
.m-list{left:9px;top:184px;width:170px}
.m-li{display:flex;gap:6px;height:51px;padding-top:3px;border-bottom:1px solid var(--line)}
.m-li .ph{width:30px;height:30px;flex:none;border-radius:2px}
.m-li h4{font-size:5.5px;font-weight:600;line-height:1.6}
.m-li p{font-size:4.5px;color:var(--muted);margin-top:3px}
.m-eps{left:0;top:459px;width:184px;height:687px}
.m-title{position:absolute;left:0;width:100%;text-align:center;font-size:9px;font-weight:600}
.m-ep{position:absolute;left:20px;width:146px}
.m-ep .ph{height:115px;border-radius:4px}
.m-ep .d{font-size:4.5px;margin-top:10px}
.m-ep .t{font-size:5px;font-weight:600;line-height:1.6;margin-top:4px}
.m-ep .s{font-size:4.5px;color:#bbb;margin-top:4px}
.m-card{position:absolute;left:11px;width:157px;background:#fff;border-radius:4px;box-shadow:0 1px 6px rgba(0,0,0,.14);padding:8px}
.m-card .ph{height:108px;border-radius:2px}
.m-card h5{font-size:5px;font-weight:400;line-height:1.7;margin-top:8px}
.m-card p{font-size:5px;color:#666;margin-top:6px}
.m-shorts{left:0;top:2453px;width:184px;height:1112px}
.m-stxt{position:absolute;left:20px;width:144px;text-align:center;font-size:7px;line-height:1.6;color:#e8e8e8}
.m-simg{position:absolute;left:25px;width:132px;border-radius:3px}
.m-sover{position:absolute;left:0;right:0;bottom:18px;text-align:center;font-size:7px;line-height:1.6;color:#fff}
.m-footer{left:0;top:4260px;width:184px;height:184px}
</style>
</head>
<body>
<div class="canvas">

<!-- DESKTOP -->
<section class="board desktop">
  <header class="abs d-header">
    <div class="brand" style="position:absolute;left:81px;top:18px;font-size:12px;width:90px">Tin Bell Raven</div>
    <nav class="d-nav">
      <a class="on" style="left:321px">HOME</a>
      <a style="left:390px">VIDEOS</a>
      <a style="left:463px">DONATE</a>
      <a style="left:535px">MERCH</a>
      <a style="left:604px">ABOUT</a>
    </nav>
    <div class="btn-login">LOGIN / SIGNUP</div>
  </header>

  <section class="abs d-hero">
    <div class="abs hero-card ph-hero" role="img" aria-label="Singer performing at a studio microphone under red and blue light">
      <span class="badge-new">NEW</span>
      <span class="watch">WATCH NOW</span>
      <div class="dashes"><i></i><i></i><i></i><i></i><i></i><i></i><i></i><i class="on"></i></div>
    </div>
    <div class="abs hero-list">
      <div class="hl-item"><div class="ph ph-hero" role="img" aria-label="Track thumbnail"></div><div><h4>New Track Drop: Whiskey &amp; Wires New Track Drop: Whiskey &amp; Wires</h4><p>Dropping fire every Friday — new single</p></div></div>
      <div class="hl-item"><div class="ph ph-grey" role="img" aria-label="Track thumbnail"></div><div><h4>New Track Drop: Whiskey &amp; Wires New Track Drop: Whiskey &amp; Wires</h4><p>Dropping fire every Friday — new single</p></div></div>
      <div class="hl-item"><div class="ph ph-warm" role="img" aria-label="Track thumbnail"></div><div><h4>New Track Drop: Whiskey &amp; Wires New Track Drop: Whiskey &amp; Wires</h4><p>Dropping fire every Friday — new single</p></div></div>
      <div class="hl-item"><div class="ph ph-stage" role="img" aria-label="Track thumbnail"></div><div><h4>New Track Drop: Whiskey &amp; Wires New Track Drop: Whiskey &amp; Wires</h4><p>Dropping fire every Friday — new single</p></div></div>
      <div class="hl-item" style="border:0"><div class="ph ph-purple" role="img" aria-label="Track thumbnail"></div><div><h4>New Track Drop: Whiskey &amp; Wires New Track Drop: Whiskey &amp; Wires</h4><p>Dropping fire every Friday — new single</p></div></div>
    </div>
  </section>

  <section class="abs d-episodes dark">
    <h2 class="abs sec-title" style="left:81px;top:55px">LATEST EPISODES</h2>
    <div class="abs view-all" style="left:710px;top:66px">VIEW ALL
      <svg width="12" height="8" viewBox="0 0 12 8"><path d="M0 4h10M7 1l3 3-3 3" stroke="#fff" fill="none" stroke-width="1.2"/></svg></div>
    <article class="ep-card" style="left:81px"><div class="ph ph-warm" role="img" aria-label="Vintage microphone with warm stage lights"></div><div class="ep-date">OCT 29, 2025</div><div class="ep-title">Dropping fire every Friday — new single every week. Stay tuned!</div><div class="ep-desc">Learn about a few of the fascinating women</div></article>
    <article class="ep-card" style="left:326px"><div class="ph ph-studio" role="img" aria-label="Artist recording in a warm studio"></div><div class="ep-date">OCT 29, 2025</div><div class="ep-title">AI Meets Country Rap — Behind the Sound Revolution</div><div class="ep-desc">Every bar tells a story — from long nights,</div></article>
    <article class="ep-card" style="left:571px"><div class="ph ph-blue" role="img" aria-label="Producer at glowing studio monitors"></div><div class="ep-date">OCT 29, 2025</div><div class="ep-title">Life on the Dirt Road: Inspiration Behind the Lyrics</div><div class="ep-desc">Every bar tells a story — from long nights,</div></article>
  </section>

  <div class="abs ad-label">ADVERTISEMENT</div>
  <div class="abs ad">
    <div class="ad-photo" role="img" aria-label="Documentary promo photo"></div>
    <div class="ad-body">
      <span class="ad-q">What Makes a Home?</span>
      <div class="ad-head">One man's journey to answer<br>the question of a generation</div>
      <div class="ad-sub">Stream Now on <b>EVENING LEDGER</b></div>
    </div>
  </div>

  <h2 class="abs news-head">LATEST NEWS</h2>
  <article class="news-card" style="left:81px;top:1248px"><div class="ph ph-blue" role="img" aria-label="Band on stage in a dim studio"></div><h5>Life on the Dirt Road: Inspiration Behind the LyricsLife on the Dirt Road: Inspiration Behind the Lyrics</h5><p>By Cole Harlan | 13hrs ago</p></article>
  <article class="news-card" style="left:318px;top:1248px"><div class="ph ph-studio" role="img" aria-label="Hands on a mixing desk"></div><h5>The Raven's promise: new beats, new bars, no breaks. Check out this week's drop and stay tuned for next</h5><p>By Cole Harlan | 13hrs ago</p></article>
  <article class="news-card" style="left:555px;top:1248px"><div class="ph ph-grey" role="img" aria-label="Producer at computer screens"></div><h5>Discover how Tin Bell Raven uses AI to amplify the storytelling — from crafting sounds that hit harder to</h5><p>By Cole Harlan | 13hrs ago</p></article>
  <article class="news-card" style="left:81px;top:1530px"><div class="ph ph-blue" role="img" aria-label="Producer at a lit mixing console"></div><h5>Life on the Dirt Road: Inspiration Behind the LyricsLife on the Dirt Road: Inspiration Behind the Lyrics</h5><p>By Cole Harlan | 13hrs ago</p></article>
  <article class="news-card" style="left:318px;top:1530px"><div class="ph ph-blue" role="img" aria-label="Studio console glowing in teal"></div><h5>Every bar tells a story — from long nights, hard work, and wild rides to moments that shaped the Raven's</h5><p>By Cole Harlan | 13hrs ago</p></article>
  <article class="news-card" style="left:555px;top:1530px"><div class="ph ph-purple" role="img" aria-label="Mixing desk under purple lights"></div><h5>The Raven's promise: new beats, new bars, no breaks. Check out this week's drop and stay tuned for next</h5><p>By Cole Harlan | 13hrs ago</p></article>

  <section class="abs d-shorts dark">
    <h2 class="abs sec-title" style="left:81px;top:55px">SHORTS</h2>
    <p class="short-txt" style="left:81px;top:112px;width:159px">Country rap with attitude — blending outlaw soul and high-tech energy.</p>
    <div class="short-img ph-warm" style="left:81px;top:176px;width:159px;height:145px" role="img" aria-label="Singer in headphones by a microphone"></div>
    <div class="short-img ph-studio" style="left:256px;top:124px;width:159px;height:200px" role="img" aria-label="Microphone in a studio"><span class="short-over">Country rap with attitude — blending outlaw soul and</span></div>
    <p class="short-txt" style="left:431px;top:112px;width:159px">Country rap with attitude — blending outlaw soul and high-tech energy.</p>
    <div class="short-img ph-studio" style="left:431px;top:176px;width:159px;height:150px" role="img" aria-label="Artist at a studio keyboard"></div>
    <div class="short-img ph-grey" style="left:605px;top:124px;width:159px;height:200px" role="img" aria-label="Mixing console close-up"><span class="short-over">Country rap with attitude — blending</span></div>
    <div class="short-img ph-stage" style="left:781px;top:124px;width:80px;height:200px" role="img" aria-label="Concert crowd and stage lights"></div>
  </section>

  <article class="news-card" style="left:81px;top:2321px"><div class="ph ph-blue" role="img" aria-label="Producer at a lit mixing console"></div><h5>Life on the Dirt Road: Inspiration Behind the LyricsLife on the Dirt Road: Inspiration Behind the Lyrics</h5><p>By Cole Harlan | 13hrs ago</p></article>
  <article class="news-card" style="left:318px;top:2321px"><div class="ph ph-blue" role="img" aria-label="Studio console glowing in teal"></div><h5>Every bar tells a story — from long nights, hard work, and wild rides to moments that shaped the Raven's</h5><p>By Cole Harlan | 13hrs ago</p></article>
  <article class="news-card" style="left:555px;top:2321px"><div class="ph ph-purple" role="img" aria-label="Mixing desk under purple lights"></div><h5>The Raven's promise: new beats, new bars, no breaks. Check out this week's drop and stay tuned for next</h5><p>By Cole Harlan | 13hrs ago</p></article>
  <div class="abs more">VIEW MORE STORIES<br><svg width="10" height="8" viewBox="0 0 10 8"><path d="M1 2l4 4 4-4" stroke="#1b1b1b" fill="none" stroke-width="1.2"/></svg></div>

  <footer class="abs d-footer dark">
    <div class="brand" style="position:absolute;left:81px;top:40px;font-size:22px;width:140px;line-height:1.1;color:#c5283a">Tin Bell Raven</div>
    <nav class="f-nav" style="left:460px;top:40px"><span>HOME</span><span>VIDEOS</span><span>DONATE</span><span>MERCH</span><span>ABOUT</span></nav>
    <div class="socials" style="left:656px;top:74px"><i></i><i></i><i></i><i></i></div>
    <div class="f-rule" style="left:81px;right:81px;top:152px"></div>
    <div class="copy" style="left:0;width:854px;top:166px">© 2025 Tin Bell Raven. All rights reserved.</div>
  </footer>
</section>

<!-- MOBILE -->
<section class="board mobile">
  <header class="abs m-header">
    <div class="brand" style="font-size:7px">Tin Bell Raven</div>
    <div class="burger"><i></i><i></i><i></i></div>
  </header>
  <div class="abs m-hero ph-hero" role="img" aria-label="Singer performing at a studio microphone">
    <span class="badge-new" style="left:8px;top:8px;font-size:4px;padding:1px 4px">NEW</span>
    <span class="watch" style="left:55px;top:94px;width:52px;height:12px;font-size:4px;border-radius:3px">WATCH NOW</span>
  </div>
  <div class="abs m-list">
    <div class="m-li"><div class="ph ph-hero" role="img" aria-label="Track thumbnail"></div><div><h4>New Track Drop: Whiskey &amp; Wires New Track Drop: Whiskey &amp; Wires</h4><p>Dropping fire every Friday — new single</p></div></div>
    <div class="m-li"><div class="ph ph-grey" role="img" aria-label="Track thumbnail"></div><div><h4>New Track Drop: Whiskey &amp; Wires New Track Drop: Whiskey &amp; Wires</h4><p>Dropping fire every Friday — new single</p></div></div>
    <div class="m-li"><div class="ph ph-warm" role="img" aria-label="Track thumbnail"></div><div><h4>New Track Drop: Whiskey &amp; Wires New Track Drop: Whiskey &amp; Wires</h4><p>Dropping fire every Friday — new single</p></div></div>
    <div class="m-li"><div class="ph ph-stage" role="img" aria-label="Track thumbnail"></div><div><h4>New Track Drop: Whiskey &amp; Wires New Track Drop: Whiskey &amp; Wires</h4><p>Dropping fire every Friday — new single</p></div></div>
    <div class="m-li" style="border:0"><div class="ph ph-purple" role="img" aria-label="Track thumbnail"></div><div><h4>New Track Drop: Whiskey &amp; Wires New Track Drop: Whiskey &amp; Wires</h4><p>Dropping fire every Friday — new single</p></div></div>
  </div>

  <section class="abs m-eps dark">
    <h2 class="m-title" style="top:36px">LATEST EPISODES</h2>
    <article class="m-ep" style="top:67px"><div class="ph ph-warm" role="img" aria-label="Vintage microphone with warm lights"></div><div class="d">OCT 29, 2025</div><div class="t">Dropping fire every Friday — new single every week. Stay tuned!</div><div class="s">Learn about a few of the fascinating women</div></article>
    <article class="m-ep" style="top:263px"><div class="ph ph-studio" role="img" aria-label="Artist recording in a studio"></div><div class="d">OCT 29, 2025</div><div class="t">AI Meets Country Rap — Behind the Sound Revolution</div><div class="s">Every bar tells a story — from long nights,</div></article>
    <article class="m-ep" style="top:459px"><div class="ph ph-blue" role="img" aria-label="Producer at glowing monitors"></div><div class="d">OCT 29, 2025</div><div class="t">Life on the Dirt Road: Inspiration Behind the Lyrics</div><div class="s">Every bar tells a story — from long nights,</div></article>
    <div class="abs view-all" style="left:68px;top:652px;font-size:5px">VIEW ALL <svg width="8" height="6" viewBox="0 0 12 8"><path d="M0 4h10M7 1l3 3-3 3" stroke="#fff" fill="none" stroke-width="1.4"/></svg></div>
  </section>

  <div class="abs" style="left:11px;top:1167px;width:162px;height:20px;display:flex">
    <div style="width:48px;background:linear-gradient(90deg,#5a2a1a,#c89060)" role="img" aria-label="Documentary promo photo"></div>
    <div style="flex:1;background:var(--ad-blue)"></div>
  </div>
  <h2 class="m-title" style="top:1213px;color:var(--ink)">LATEST NEWS</h2>
  <article class="m-card" style="top:1255px"><div class="ph ph-blue" role="img" aria-label="Band in a dim studio"></div><h5>Life on the Dirt Road: Inspiration Behind the LyricsLife on the Dirt Road: Inspiration Behind the Lyrics</h5><p>By Cole Harlan | 13hrs ago</p></article>
  <article class="m-card" style="top:1449px"><div class="ph ph-studio" role="img" aria-label="Hands on a mixing desk"></div><h5>The Raven's promise: new beats, new bars, no breaks. Check out this week's drop and stay tuned for next</h5><p>By Cole Harlan | 13hrs ago</p></article>
  <article class="m-card" style="top:1643px"><div class="ph ph-grey" role="img" aria-label="Producer at computer screens"></div><h5>Discover how Tin Bell Raven uses AI to amplify the storytelling — from crafting sounds that hit harder to</h5><p>By Cole Harlan | 13hrs ago</p></article>
  <article class="m-card" style="top:1837px"><div class="ph ph-blue" role="img" aria-label="Producer at a lit console"></div><h5>Life on the Dirt Road: Inspiration Behind the LyricsLife on the Dirt Road: Inspiration Behind the Lyrics</h5><p>By Cole Harlan | 13hrs ago</p></article>
  <article class="m-card" style="top:2031px"><div class="ph ph-blue" role="img" aria-label="Studio console in teal"></div><h5>Every bar tells a story — from long nights, hard work, and wild rides to moments that shaped the Raven's</h5><p>By Cole Harlan | 13hrs ago</p></article>
  <article class="m-card" style="top:2225px"><div class="ph ph-purple" role="img" aria-label="Mixing desk under purple lights"></div><h5>The Raven's promise: new beats, new bars, no breaks. Check out this week's drop and stay tuned for next</h5><p>By Cole Harlan | 13hrs ago</p></article>

  <section class="abs m-shorts dark">
    <h2 class="m-title" style="top:40px">SHORTS</h2>
    <p class="m-stxt" style="top:72px">Country rap with attitude — blending outlaw soul and high-tech energy.</p>
    <div class="m-simg ph-warm" style="top:143px;height:124px" role="img" aria-label="Singer in headphones"></div>
    <div class="m-simg ph-studio" style="top:284px;height:180px" role="img" aria-label="Microphone in a studio"><span class="m-sover">Country rap with attitude — blending outlaw soul and high-tech energy.</span></div>
    <p class="m-stxt" style="top:494px">Country rap with attitude — blending outlaw soul and</p>
    <div class="m-simg ph-studio" style="top:549px;height:129px" role="img" aria-label="Artist at a studio keyboard"></div>
    <div class="m-simg ph-grey" style="top:703px;height:168px" role="img" aria-label="Mixing console close-up"><span class="m-sover">Country rap with attitude — blending</span></div>
    <div class="m-simg ph-stage" style="top:896px;height:168px" role="img" aria-label="Concert crowd and stage lights"></div>
  </section>

  <article class="m-card" style="top:3597px"><div class="ph ph-blue" role="img" aria-label="Producer at a lit console"></div><h5>Life on the Dirt Road: Inspiration Behind the LyricsLife on the Dirt Road: Inspiration Behind the Lyrics</h5><p>By Cole Harlan | 13hrs ago</p></article>
  <article class="m-card" style="top:3800px"><div class="ph ph-blue" role="img" aria-label="Studio console in teal"></div><h5>Every bar tells a story — from long nights, hard work, and wild rides to moments that shaped the Raven's</h5><p>By Cole Harlan | 13hrs ago</p></article>
  <article class="m-card" style="top:4006px"><div class="ph ph-purple" role="img" aria-label="Mixing desk under purple lights"></div><h5>The Raven's promise: new beats, new bars, no breaks. Check out this week's drop and stay tuned for next</h5><p>By Cole Harlan | 13hrs ago</p></article>
  <div class="abs more" style="top:4208px;width:184px;font-size:6px">VIEW MORE STORIES<br><svg width="7" height="6" viewBox="0 0 10 8"><path d="M1 2l4 4 4-4" stroke="#1b1b1b" fill="none" stroke-width="1.4"/></svg></div>

  <footer class="abs m-footer dark">
    <div class="brand" style="position:absolute;left:0;width:184px;justify-content:center;top:50px;font-size:12px;color:#c5283a">Tin Bell Raven</div>
    <nav class="f-nav" style="left:0;width:184px;justify-content:center;top:122px;gap:9px;font-size:4px"><span>HOME</span><span>VIDEOS</span><span>DONATE</span><span>MERCH</span><span>ABOUT</span></nav>
    <div class="socials" style="left:62px;top:137px;gap:4px"><i style="width:12px;height:12px"></i><i style="width:12px;height:12px"></i><i style="width:12px;height:12px"></i><i style="width:12px;height:12px"></i></div>
    <div class="f-rule" style="left:10px;right:10px;top:162px"></div>
    <div class="copy" style="left:0;width:184px;top:167px;font-size:4px">© 2025 Tin Bell Raven. All rights reserved.</div>
  </footer>
</section>

</div>
</body>
</html>
```